Business Card for Auto Dealership - Clean, sharp and professional

Please use the maroon logo with the grey background. Need a sharp, clean and professional business card for an Auto Dealer. In the files provides there is three different logos. I have not decided which one to go with yet. Right now I am favoring the grey/silver background. I would like my contact info on there and the website as well. I feel like less is more and want something simple, clean and sharp. Thank you in advance for your tie and effort! I also need email signature, letterhead, etc after this

Target Market(s)

Car buyers

Industry/Entity Type

Automotive

Contact Information for Business Card

Drew
555-214-7730
www.BriarvaleAutoLink.example
Drew@BriarvaleAutoLink.example

Font styles to use
Serif
Sans Serif

Requirements
Must have
• Please use the maroon logo with the grey background. Business Card Details and logo from files. Please stick to the logo colors

```html
<!DOCTYPE html>
<html lang="en">
<head>
<meta charset="utf-8">
<title>Briarvale Auto Link – Business Card</title>
<link rel="stylesheet" href="https://fonts.googleapis.com/css2?family=Michroma&family=Arimo:wght@400;700&display=swap">
<style>
  :root {
    --maroon: #5a1417;
    --maroon-soft: #6e2226;
    --card: #f5f5f5;
    --card-edge: #e2e2e2;
    --ghost: #ebe8e8;
    --backdrop: #2b2b2b;
  }
  * { box-sizing: border-box; margin: 0; padding: 0; }
  html, body { width: 1200px; height: 852px; overflow: hidden; }
  body {
    background: var(--backdrop);
    display: flex;
    align-items: center;
    justify-content: center;
    gap: 40px;
    font-family: "Arimo", Arial, sans-serif;
    color: var(--maroon);
  }
  .card {
    position: relative;
    width: 540px;
    height: 309px;
    border-radius: 22px;
    background: linear-gradient(135deg, #ffffff 0%, var(--card) 55%, var(--card-edge) 100%);
    overflow: hidden;
  }
  .brand-name {
    font-family: "Michroma", "Arial Black", sans-serif;
    color: var(--maroon);
    line-height: 1;
    white-space: nowrap;
  }
  .brand-name .primary { display: block; font-size: 34px; letter-spacing: 1px; }
  .brand-name .secondary { display: block; font-size: 11px; letter-spacing: 8.5px; margin-top: 6px; }

  /* Front */
  .card-front .ghost-ring {
    position: absolute;
    left: 120px; top: -20px;
    width: 300px; height: 300px;
    border-radius: 50%;
    border: 34px solid var(--ghost);
  }
  .card-front .lockup {
    position: absolute;
    left: 50%; top: 50%;
    transform: translate(-50%, -50%);
    display: flex;
    align-items: center;
    gap: 18px;
  }
  .brand-dot {
    width: 70px; height: 70px;
    border-radius: 50%;
    background: var(--maroon);
    flex: none;
  }

  /* Back */
  .card-back .brand-name {
    position: absolute;
    left: 36px; top: 62px;
  }
  .card-back .brand-name .primary { font-size: 30px; }
  .card-back .brand-name .secondary { font-size: 10px; letter-spacing: 7.5px; }
  .card-back .brand-ring {
    position: absolute;
    right: 30px; top: 40px;
    width: 190px; height: 190px;
    border-radius: 50%;
    border: 26px solid var(--maroon);
    box-shadow: 0 0 0 14px var(--ghost);
  }
  .contact {
    position: absolute;
    left: 36px; bottom: 34px;
  }
  .contact-name {
    font-family: "Michroma", "Arial Black", sans-serif;
    font-size: 22px;
    letter-spacing: 2px;
    margin-bottom: 8px;
  }
  .contact-phone {
    display: flex;
    align-items: center;
    gap: 6px;
    font-size: 20px;
    margin-bottom: 8px;
  }
  .contact-phone .divider { width: 2px; height: 20px; background: var(--maroon); }
  .contact-line { font-size: 13px; line-height: 1.45; color: var(--maroon-soft); }
</style>
</head>
<body>
  <section class="card card-front">
    <div class="ghost-ring" aria-hidden="true"></div>
    <div class="lockup">
      <div class="brand-dot" aria-hidden="true"></div>
      <div class="brand-name">
        <span class="primary">BRIARVALE</span>
        <span class="secondary">AUTO LINK</span>
      </div>
    </div>
  </section>

  <section class="card card-back">
    <div class="brand-name">
      <span class="primary">BRIARVALE</span>
      <span class="secondary">AUTO LINK</span>
    </div>
    <div class="brand-ring" aria-hidden="true"></div>
    <div class="contact">
      <p class="contact-name">DREW</p>
      <p class="contact-phone">
        <svg width="18" height="16" viewBox="0 0 18 16" aria-hidden="true">
          <path d="M2 5 Q9 -1 16 5 L14 7 L11.5 5.5 L11.5 4 Q9 3 6.5 4 L6.5 5.5 L4 7 Z" fill="var(--maroon)"/>
          <rect x="4" y="8" width="10" height="7" rx="1.5" fill="var(--maroon)"/>
        </svg>
        <span class="divider" aria-hidden="true"></span>
        <span>555-214-7730</span>
      </p>
      <p class="contact-line">Drew@BriarvaleAutoLink.example</p>
      <p class="contact-line">www.BriarvaleAutoLink.example</p>
    </div>
  </section>
</body>
</html>
```